One-Page Redesign (Member's Area of Conference-Call Service)

Please take my mockup (THE ATTACHED PNG FILE) and make it look like a modern, cool, professional SaaS. Only restriction is you have to use free web fonts. And the fonts shouldn't have weird things like some letters or numbers being odd-sized.

If we work well together, I have an infinite amount of design projects for you to do.

Target Market(s)

Small Business Owners

Industry/Entity Type

Call

Number of Pages Required

1 page

Font styles to use
Sans Serif

Colors

Designer to choose colors to be used in the design.

Requirements
Must have
• It must look like a single, cohesive design -- with the menu and the content working together. It must be readable. It must be organized. It must give people an awesome first impression
Nice to have
• I'd like it to feel welcoming, not cold
Should not have
• It should not look like a damn template... It should not look amateurish

```html
<!DOCTYPE html>
<html lang="en">
<head>
<meta charset="utf-8">
<title>Account</title>
<link href="https://fonts.googleapis.com/css2?family=Roboto:wght@400;500;700&family=Work+Sans:wght@600;700&display=swap" rel="stylesheet">
<style>
  :root{
    --orange:#e28a22;
    --sidebar:#333333;
    --divider:#464646;
    --navy:#3c475c;
    --ink:#3a3a3a;
    --body:#4a4a4a;
    --page:#f3f3f3;
    --card:#ffffff;
    --line:#e4e4e4;
    --white:#ffffff;
  }
  *{box-sizing:border-box;margin:0;padding:0}
  html,body{width:1200px;height:750px;overflow:hidden}
  body{font-family:"Roboto",sans-serif;background:var(--page);position:relative;color:var(--ink)}

  .sidebar{position:absolute;left:0;top:0;width:235px;height:750px;background:var(--sidebar)}
  .brand{height:103px;background:var(--orange);display:flex;align-items:center;justify-content:center;gap:10px}
  .brand-dot{width:14px;height:14px;border-radius:50%;background:var(--white)}
  .brand-name{font-family:"Work Sans",sans-serif;font-weight:700;font-size:30px;color:var(--white);letter-spacing:.5px}
  .member{height:91px;padding:22px 9px 0;border-bottom:1px solid var(--divider)}
  .member-name{font-family:"Work Sans",sans-serif;font-weight:700;font-size:23px;color:var(--white);letter-spacing:.8px}
  .member-id{font-family:"Work Sans",sans-serif;font-weight:600;font-size:13px;color:var(--white);margin-top:5px;letter-spacing:.5px}
  .nav-item{height:78.5px;display:flex;align-items:center;padding-left:10px;border-bottom:1px solid var(--divider);color:var(--white);font-size:14px;letter-spacing:1px}
  .nav-icon{width:57px;height:57px;background:var(--orange);border-radius:3px;display:flex;align-items:center;justify-content:center;margin-right:21px}
  .nav-icon svg{width:30px;height:30px;fill:none;stroke:var(--white);stroke-width:1.6;stroke-linecap:round;stroke-linejoin:round}
  .nav-item.is-active{background:var(--orange);height:75px;border-bottom:none}
  .nav-item.is-active .nav-icon{background:var(--white)}
  .nav-item.is-active .nav-icon svg{stroke:var(--orange)}

  .topbar{position:absolute;left:235px;top:0;right:0;height:47px;background:var(--white);border-bottom:1px solid var(--line);display:flex;align-items:center;justify-content:space-between;padding:0 12px 0 12px}
  .page-title{font-family:"Work Sans",sans-serif;font-weight:700;font-size:21px;color:var(--navy);letter-spacing:1px}
  .power svg{width:20px;height:20px;fill:none;stroke:#777;stroke-width:2.2;stroke-linecap:round}
  .crumbs{position:absolute;left:250px;top:69px;font-size:12px;color:var(--navy);letter-spacing:.3px}

  .grid{position:absolute;left:248px;top:104px;display:grid;grid-template-columns:repeat(3,306px);grid-auto-rows:193px;column-gap:12px;row-gap:13px}
  .card{background:var(--card);border:1px solid #ebebeb;text-align:center;padding-top:25px}
  .card.is-active{border-color:var(--orange);box-shadow:0 2px 10px rgba(0,0,0,.12)}
  .card-icon{width:72px;height:72px;display:block;margin:0 auto}
  .card-icon *{fill:none;stroke:var(--navy);stroke-width:4;stroke-linecap:round;stroke-linejoin:round}
  .card-icon .solid{fill:var(--navy);stroke:none}
  .card.is-active .card-icon *{stroke:var(--orange)}
  .card.is-active .card-icon .solid{fill:var(--orange)}
  .card-title{font-family:"Work Sans",sans-serif;font-weight:700;font-size:18px;letter-spacing:1.5px;color:var(--ink);margin-top:17px}
  .card.is-active .card-title{color:var(--orange)}
  .card-text{font-size:12.5px;line-height:15px;color:var(--body);letter-spacing:.4px;margin:14px 14px 0}
</style>
</head>
<body>
<aside class="sidebar">
  <div class="brand"><span class="brand-dot"></span><span class="brand-name">LOGO</span></div>
  <div class="member">
    <div class="member-name">Lorem Ipsum</div>
    <div class="member-id">Member ID:2102545</div>
  </div>
  <nav>
    <div class="nav-item"><span class="nav-icon"><svg viewBox="0 0 30 30"><path d="M8 5l4 5-2 3c1 3 4 6 7 7l3-2 5 4-2 3c-8 1-18-9-17-17z"/><path d="M17 6a7 7 0 0 1 7 7M17 2a11 11 0 0 1 11 11"/></svg></span>PHONE CONFRENCE</div>
    <div class="nav-item"><span class="nav-icon"><svg viewBox="0 0 30 30"><rect x="4" y="6" width="22" height="20" rx="1"/><path d="M4 11h22M9 3v5M21 3v5M8 15h14M8 19h14M8 23h14M11 13v12M15 13v12M19 13v12"/></svg></span>SCHEDULED EVENTS</div>
    <div class="nav-item"><span class="nav-icon"><svg viewBox="0 0 30 30"><path d="M11 16c0-2 4-3 8-3s8 1 8 3-4 3-8 3-8-1-8-3zM12 17l1 9h12l1-9M3 26l10-16M22 4v4M20 6h4M26 9v3"/></svg></span>COOL STUFF</div>
    <div class="nav-item"><span class="nav-icon"><svg viewBox="0 0 30 30"><path d="M10 10a5 5 0 1 1 7 4c-2 1-2 3-2 5" stroke-width="2.6"/><path d="M15 24v1" stroke-width="3"/></svg></span>HELP &amp; TRAINING</div>
    <div class="nav-item is-active"><span class="nav-icon"><svg viewBox="0 0 30 30"><circle cx="15" cy="11" r="5"/><path d="M5 26c0-6 4-9 10-9s10 3 10 9z"/></svg></span>ACCOUNT</div>
  </nav>
</aside>

<header class="topbar">
  <h1 class="page-title">ACCOUNT</h1>
  <span class="power"><svg viewBox="0 0 20 20"><path d="M10 2v7"/><path d="M5.5 5a7 7 0 1 0 9 0"/></svg></span>
</header>
<div class="crumbs">Home / Account</div>

<main class="grid">
  <div class="card is-active">
    <svg class="card-icon" viewBox="0 0 72 72"><path d="M9 28A28 28 0 0 1 62 26"/><path d="M63 44A28 28 0 0 1 10 46"/><path d="M55 25l7 1 1-7M17 47l-7-1-1 7"/><path d="M22 28c8 3 18-2 28 2v13c-10-4-20 1-28-2z" stroke-width="3"/><circle cx="36" cy="35" r="4" stroke-width="2.5"/></svg>
    <div class="card-title">CHANGE PLAN</div>
    <p class="card-text">Click here to change your service plan or cancel/ suspend service.</p>
  </div>
  <div class="card">
    <svg class="card-icon" viewBox="0 0 72 72"><path d="M9 28A28 28 0 0 1 62 26"/><path d="M63 44A28 28 0 0 1 10 46"/><path d="M55 25l7 1 1-7M17 47l-7-1-1 7"/><circle cx="27" cy="36" r="6"/><path d="M33 36h16M40 36v5M45 36v5"/></svg>
    <div class="card-title">CHANGE PASSWORD</div>
    <p class="card-text">Click here to change your password.</p>
  </div>
  <div class="card">
    <svg class="card-icon" viewBox="0 0 72 72"><path d="M9 28A28 28 0 0 1 62 26"/><path d="M63 44A28 28 0 0 1 10 46"/><path d="M55 25l7 1 1-7M17 47l-7-1-1 7"/><rect x="28" y="27" width="22" height="16" stroke-width="3"/><path d="M28 27l11 9 11-9M18 33h6M20 38h5" stroke-width="3"/></svg>
    <div class="card-title">CHANGE EMAIL</div>
    <p class="card-text">Click here to change your email assosiaged with the account.</p>
  </div>
  <div class="card">
    <svg class="card-icon" viewBox="0 0 72 72"><path d="M9 28A28 28 0 0 1 62 26"/><path d="M63 44A28 28 0 0 1 10 46"/><path d="M55 25l7 1 1-7M17 47l-7-1-1 7"/><rect x="22" y="27" width="30" height="19" rx="2" stroke-width="3"/><path d="M22 32h30M26 40h6" stroke-width="3"/><rect class="solid" x="40" y="37" width="8" height="5" rx="2"/></svg>
    <div class="card-title">CHANGE BILLING INFO</div>
    <p class="card-text">Click here to update or change the credit card on file for your account.</p>
  </div>
  <div class="card">
    <svg class="card-icon" viewBox="0 0 72 72"><circle cx="36" cy="36" r="32"/><path d="M29 22h11l5 5v22H29z" stroke-width="2.5"/><path d="M33 29h8M33 34h8M33 39h8M24 44l3 3 5-6" stroke-width="2.5"/></svg>
    <div class="card-title">VIEW INVOICES</div>
    <p class="card-text">Click here to view previously paid invoices.</p>
  </div>
  <div class="card">
    <svg class="card-icon" viewBox="0 0 72 72"><circle cx="36" cy="36" r="32"/><circle class="solid" cx="28" cy="30" r="6"/><circle class="solid" cx="44" cy="30" r="6"/><path class="solid" d="M17 46c0-6 5-9 11-9s11 3 11 9zM33 46c0-6 5-9 11-9s11 3 11 9z"/><circle class="solid" cx="36" cy="28" r="7"/><path class="solid" d="M24 47c0-7 5-11 12-11s12 4 12 11z"/></svg>
    <div class="card-title">AFFILIATES</div>
    <p class="card-text">Click here get information about your affilate account and how to earn money promoting Ringwell Conference.</p>
  </div>
</main>
</body>
</html>
```